Fin-Tech Firm Captivating Business Card Design

We need a logo design as well to compliment this business card.

We are a new startup based in Singapore called 'Pardeo Technologies'.

We develop an array of financial solutions ranging from payment convenience to forex trading and remittance.

Our initial product is Mavo - an application which allows user to pre-order food items which would be ready for pickup upon arrival.

We would like to see designs being in black and silver or whatever that looks appealing and exudes a fun and professional feel.

We're not picky as long as it doesn't look like common business cards will do.

I do have a current logo which i do not really like. It will be attached for reference sake

Info:

Pardeo Technologies Pte. Ltd.
Company Registration no. 208716392K

FILE TO BE IN .AI and .PSD

Target Market(s)

-F&B (Online-Ordering)
-Finance(P2P Lending and Forex)

Industry/Entity Type

Finance

Contact Information for Business Card

Name
Position
Contact
Email
Address: 27 Corwen Street, Meridale Tower, #14-05 Singapore 058214

Harlan Webb
Founder, Managing Director
+65 90481736
harlan.w@pardeotech.com

Wei Tan
Founder, Executive Director
+65 93570284
wei.t@pardeotech.com

Logo Text

Pardeo Technologies

Font styles to use
Sans Serif

Requirements
Must have
• Something that has word play about link pard
• Minimalistic but also something that catches The Eye
• Gold/silver on white/black might be nice
• Animal logo ; horse, eagle, bull or bear
Nice to have
• Just make it look fun and cute
• Just a suggestion to make the Y of pardeo stand out
Should not have
• Any landmarks of singapore
• Exclude Pte. Ltd.

```html
<!DOCTYPE html>
<html lang="en">
<head>
<meta charset="utf-8">
<title>Pardeo Technologies – Business Card</title>
<link href="https://fonts.googleapis.com/css2?family=Open+Sans:wght@400;600;700&display=swap" rel="stylesheet">
<style>
  :root {
    --amber: #f2a516;
    --white: #ffffff;
    --paper: #f4f4f4;
    --grey: #8a8a8a;
    --stage: #ebe7e2;
    --shadow: rgba(0, 0, 0, 0.18);
  }
  * { box-sizing: border-box; margin: 0; padding: 0; }
  html, body {
    width: 1200px; height: 900px; overflow: hidden;
    background: var(--stage);
    font-family: "Open Sans", sans-serif;
  }
  .stage { position: relative; width: 1200px; height: 900px; }
  .card {
    position: absolute; width: 560px; height: 320px;
    border-radius: 3px; overflow: hidden;
    box-shadow: 0 14px 30px var(--shadow);
  }
  .card-front { left: 90px; top: 130px; background: var(--amber); }
  .card-back { left: 550px; top: 430px; background: var(--amber); }

  .wordmark { display: flex; align-items: center; gap: 18px; }
  .wordmark-square { flex: none; }
  .wordmark-name {
    font-weight: 400; line-height: 1; letter-spacing: 2px; text-transform: uppercase;
  }
  .wordmark-sub {
    display: block; font-weight: 400; letter-spacing: 1.5px; text-transform: uppercase;
    margin-top: 6px;
  }
  .card-front .wordmark {
    position: absolute; left: 50%; top: 50%; transform: translate(-50%, -50%);
    color: var(--white);
  }
  .card-front .wordmark-square { width: 78px; height: 78px; background: var(--white); }
  .card-front .wordmark-name { font-size: 52px; }
  .card-front .wordmark-sub { font-size: 15px; }

  .back-top {
    position: absolute; left: 0; top: 0; width: 100%; height: 168px;
    background: linear-gradient(180deg, var(--white), var(--paper));
  }
  .back-stripe {
    position: absolute; left: 0; top: 168px; width: 100%; height: 8px;
    background: var(--grey); border-top: 3px solid var(--white);
  }
  .card-back .wordmark {
    position: absolute; left: 150px; top: 40px; color: var(--amber);
  }
  .card-back .wordmark-square { width: 70px; height: 70px; background: var(--amber); }
  .card-back .wordmark-name { font-size: 44px; }
  .card-back .wordmark-sub { font-size: 13px; }

  .contact {
    position: absolute; top: 190px; color: var(--white);
    font-size: 13px; line-height: 1.55;
  }
  .contact-lines { right: 300px; text-align: right; top: 218px; }
  .contact-lines p { display: flex; justify-content: flex-end; align-items: center; gap: 6px; }
  .contact-lines svg { width: 12px; height: 12px; fill: var(--white); }
  .registration { font-weight: 700; font-size: 14px; margin-top: 6px; }
  .contact-person { left: 285px; }
  .person-name { font-weight: 700; font-size: 17px; }
  .person-role { margin-bottom: 8px; }
</style>
</head>
<body>
<main class="stage">
  <section class="card card-front">
    <div class="wordmark">
      <span class="wordmark-square"></span>
      <span>
        <span class="wordmark-name">Pardeo</span>
        <span class="wordmark-sub">Technologies Pte. Ltd</span>
      </span>
    </div>
  </section>

  <section class="card card-back">
    <div class="back-top"></div>
    <div class="back-stripe"></div>
    <div class="wordmark">
      <span class="wordmark-square"></span>
      <span>
        <span class="wordmark-name">Pardeo</span>
        <span class="wordmark-sub">Technologies Pte. Ltd</span>
      </span>
    </div>

    <div class="contact contact-lines">
      <p>+65 90481736
        <svg viewBox="0 0 24 24"><path d="M6.6 10.8a15.1 15.1 0 0 0 6.6 6.6l2.2-2.2a1 1 0 0 1 1-.25 11.4 11.4 0 0 0 3.6.57 1 1 0 0 1 1 1V20a1 1 0 0 1-1 1A17 17 0 0 1 3 4a1 1 0 0 1 1-1h3.5a1 1 0 0 1 1 1c0 1.25.2 2.45.57 3.6a1 1 0 0 1-.25 1z"/></svg>
      </p>
      <p>harlan.w@pardeotech.com
        <svg viewBox="0 0 24 24"><path d="M2 5h20v14H2z M2 5l10 8 10-8" fill="none" stroke="#fff" stroke-width="2"/></svg>
      </p>
      <p class="registration">Company Registration no. 208716392K</p>
    </div>

    <div class="contact contact-person">
      <p class="person-name">Harlan Webb</p>
      <p class="person-role">Founder, Managing Director</p>
      <p>27 Corwen Street, Meridale Tower,</p>
      <p>#14-05 Singapore 058214</p>
    </div>
  </section>
</main>
</body>
</html>
```